Skyward Rovers

I would like to re-fresh my existing web page with something more elegant and professional and what will match with my new logo. From the page it should be clearly seen that I organize and sell flying safaris, it should not be tightened only to Africa, should be general.

Page to be re-freshed:
http://skyward-rovers.example

Target Market(s)

Pilots and non-pilots who are going to have a bush flying safari in Africa

Industry/Entity Type

It Professional

```html
<!DOCTYPE html>
<html lang="en">
<head>
<meta charset="utf-8">
<title>Skyward Rovers – Flying Safaris</title>
<link rel="stylesheet" href="https://fonts.googleapis.com/css2?family=Ubuntu:wght@400;500;700&display=swap">
<style>
  :root {
    --canvas: #ffffff;
    --page-top: #f7f9f1;
    --page-mid: #e9f1d2;
    --page-bottom: #7aae22;
    --panel: #f4f8e9;
    --ink: #1e1e16;
    --accent-red: #a3201f;
    --logo-ink: #2b2b2b;
    --hero-dark: #5a3f14;
    --hero-mid: #b9862e;
    --hero-light: #d9b36a;
    --falls-green: #2f5a28;
    --falls-mist: #cfd9d6;
    --social-blue: #2a56a8;
    --social-teal: #3aa7b6;
    --white: #ffffff;
  }
  * { margin: 0; padding: 0; box-sizing: border-box; }
  html, body {
    width: 1200px; height: 1200px; overflow: hidden;
    background: var(--canvas);
    font-family: "Ubuntu", "Trebuchet MS", sans-serif;
    color: var(--ink);
  }
  .page {
    position: absolute; left: 116px; top: 103px;
    width: 977px; height: 995px;
    background: linear-gradient(180deg, var(--page-top) 0%, var(--page-top) 30%, var(--page-mid) 62%, #cfe29e 80%, var(--page-bottom) 92%, var(--page-bottom) 100%);
  }
  .brand {
    position: absolute; left: 118px; top: 50px;
    display: flex; align-items: center; gap: 12px;
    font-size: 34px; font-weight: 500; color: var(--logo-ink);
    letter-spacing: -0.5px;
  }
  .brand-mark { width: 28px; height: 28px; background: var(--accent-red); }
  .main-nav {
    position: absolute; left: 447px; top: 42px;
    display: grid; grid-template-columns: repeat(3, 120px);
    row-gap: 22px; column-gap: 5px;
    font-size: 11.5px; font-weight: 700; text-align: center;
  }
  .main-nav a { color: var(--ink); text-decoration: none; }
  .main-nav a.is-current { color: var(--accent-red); }
  .hero {
    position: absolute; left: 101px; top: 129px; width: 755px; height: 168px;
    background: linear-gradient(90deg, var(--hero-dark) 0%, var(--hero-mid) 30%, var(--hero-light) 50%, #8a8a3a 75%, #4e6a22 100%);
  }
  .hero-caption {
    position: absolute; right: 18px; bottom: 10px;
    font-size: 26px; color: var(--white); letter-spacing: 0.5px;
  }
  .content {
    position: absolute; left: 101px; top: 331px; width: 755px; height: 526px;
    background: var(--panel);
    padding: 34px 14px 0 39px;
  }
  .content h1 {
    font-size: 16px; font-weight: 500; color: var(--accent-red);
    line-height: 23px; text-transform: uppercase; margin-bottom: 17px;
  }
  .content p {
    font-size: 10.2px; font-weight: 700; line-height: 15.4px;
  }
  .intro { margin-bottom: 16px; }
  .story { display: flex; gap: 22px; margin-bottom: 16px; }
  .story p { width: 381px; }
  .falls-photo {
    width: 273px; height: 182px; flex-shrink: 0; margin-top: -6px;
    background: linear-gradient(135deg, var(--falls-green) 0%, #6f8f7a 40%, var(--falls-mist) 65%, var(--falls-green) 100%);
  }
  .site-footer .social {
    position: absolute; top: 907px; width: 26px; height: 26px; border-radius: 3px;
  }
  .social-a { left: 140px; background: var(--social-teal); }
  .social-b { left: 177px; background: var(--social-blue); }
  .contact-email {
    position: absolute; right: 161px; top: 918px;
    font-size: 12px; font-weight: 700; color: var(--white);
  }
</style>
</head>
<body>
  <div class="page">
    <header class="site-header">
      <div class="brand"><span class="brand-mark"></span>Skyward Rovers</div>
      <nav class="main-nav">
        <a class="is-current">Guided Tours</a>
        <a>Self Guided Tours</a>
        <a>Sample Tours</a>
        <a>Build Your Trip</a>
        <a>Training</a>
        <a>Gallery</a>
      </nav>
    </header>

    <section class="hero" role="img" aria-label="Close-up photograph of a lion's face in warm golden light">
      <p class="hero-caption">The Adventure of a Lifetime...</p>
    </section>

    <main class="content">
      <h1>Welcome to the world of Skyward Rovers,<br>for the adventure of a lifetime.</h1>
      <p class="intro">Skyward Rovers organises and facilitates self-fly safaris to the wildest corners of the world. What better way to see the wonders of the earth than from the pilot's seat of your own aircraft. Whether you're a PPL wanting to experience something beyond flying circuits at your local airfield, a seasoned ATP looking to recapture that passion for flying, or a traveller wanting to experience remote lands from a bird's perspective, alone or as part of a group, flying safaris offer a truly rewarding and unforgettable experience.</p>
      <div class="story">
        <p>All the most pristine and unspoiled places are without doubt off the beaten track, often only accessible by air. If it's a genuine rustic and wild experience you're after, the adventures are only waiting. But you will not find these in any guidebook or airport listing. For a pilot, as for anyone else, these adventures come at a price; usually in the form of accessibility problems and the lack of those creature comforts we've gotten so used to (air traffic control, windsocks, tarmac, avgas, aircraft mechanics etc.), not to mention unpredictable weather and far distances from help. Bush flying has entered the world of aviation and popular culture as a rugged, romantic lifestyle that combines elements of great beauty and independence with a certain degree of risk and danger.</p>
        <div class="falls-photo" role="img" aria-label="Photograph of a waterfall gorge with mist and a rainbow"></div>
      </div>
      <p>Whether setting out on your own or as part of an organised group, a safari by air is sure to be an adventure packed, rich and rewarding experience. The diversity of wildlife, tribes and cultures, stunning natural beauty and varied climates we fly to make them favourite destinations amongst many visitors, yet the mobility of flying presents the opportunity to break away from the hustle and bustle of the normal tourist trail; the freedom of the air allows us to visit those exclusive areas which are otherwise hard or nearly impossible to reach, places in which the real wilderness still emanates in every sight and sound.</p>
    </main>

    <footer class="site-footer">
      <span class="social social-a" aria-label="Social link"></span>
      <span class="social social-b" aria-label="Social link"></span>
      <span class="contact-email">info@skywardrovers.example</span>
    </footer>
  </div>
</body>
</html>
```